I need a business Card Design for my practice , i am clinical herbalist. I am a herbalist specializing in Lyme disease, autism, autoimmune diseases, difficult to cure diseasesDifficult to cure diseases. In my innovative practice i link traditional medicine, herbs with science, immunologu ,pharmacology.

Industry/Entity Type

Business

Contact Information for Business Card

My company name : OSRODEK ZIELNIKA
My name : Piotr Weltak
Name of my profession : Fitoterapeuta
In Polish language Fitoterapeuta is Herbalist .

e-mail: piotrweltak@osrodekzielnika.com
www.osrodek-zielnika.pl
phone : 574 806 215
My company adress : Dąbrowa Sękowska 14 , 38-415 Mielnik
I dont have logo .

Requirements
Nice to have
• My company

```html
<!DOCTYPE html>
<html lang="pl">
<head>
<meta charset="utf-8">
<title>Osrodek Zielnika – wizytówka</title>
<link rel="stylesheet" href="https://fonts.googleapis.com/css2?family=Bebas+Neue&family=Ubuntu:wght@400;500;700&display=swap">
<style>
  :root {
    --page-bg: #1c1c1c;
    --card-bg: #2a2a2b;
    --card-bg-light: #323233;
    --accent: #2fa83a;
    --accent-dark: #238a2d;
    --text-main: #ffffff;
    --text-soft: #d9d9d9;
  }
  * { margin: 0; padding: 0; box-sizing: border-box; }
  html, body {
    width: 1200px;
    height: 1000px;
    overflow: hidden;
    background: var(--page-bg);
  }
  .business-card {
    position: absolute;
    left: 150px;
    top: 243px;
    width: 900px;
    height: 514px;
    border-radius: 38px;
    overflow: hidden;
    background: linear-gradient(135deg, var(--card-bg) 0%, var(--card-bg-light) 55%, var(--card-bg) 100%);
    font-family: "Ubuntu", sans-serif;
    color: var(--text-main);
  }
  .bottom-band {
    position: absolute;
    left: 0; right: 0; bottom: 0;
    height: 24px;
    background: var(--accent);
  }
  .side-tab {
    position: absolute;
    left: 0;
    top: 238px;
    width: 8px;
    height: 46px;
    background: var(--accent);
  }
  .company-heading {
    position: absolute;
    left: 56px;
    top: 150px;
    font-family: "Bebas Neue", sans-serif;
    font-weight: 400;
    font-size: 60px;
    letter-spacing: 1px;
    line-height: 1;
  }
  .person {
    position: absolute;
    left: 90px;
    top: 228px;
  }
  .person-name {
    font-weight: 700;
    font-size: 32px;
    line-height: 1.1;
  }
  .person-role {
    color: var(--accent);
    font-size: 23px;
    line-height: 1.2;
  }
  .address {
    position: absolute;
    left: 110px;
    top: 306px;
    font-size: 21px;
    font-style: normal;
    line-height: 1.3;
    color: var(--text-soft);
  }
  .contact-list {
    position: absolute;
    left: 90px;
    top: 380px;
    list-style: none;
    font-size: 20px;
    color: var(--text-soft);
  }
  .contact-list li {
    display: flex;
    align-items: center;
    height: 30px;
    gap: 14px;
  }
  .contact-list svg { width: 16px; height: 16px; fill: var(--accent); flex: none; }
  .web-highlight { color: var(--accent); }
  .brand-mark {
    position: absolute;
    right: 62px;
    top: 150px;
    display: flex;
    flex-direction: column;
    align-items: center;
    gap: 22px;
  }
  .brand-dot {
    width: 92px;
    height: 92px;
    border-radius: 50%;
    background: var(--accent-dark);
  }
  .brand-name {
    font-weight: 700;
    font-size: 21px;
    letter-spacing: 0.5px;
  }
</style>
</head>
<body>
  <article class="business-card">
    <div class="side-tab"></div>
    <h1 class="company-heading">OSRODEK ZIELNIKA</h1>

    <div class="person">
      <p class="person-name">Piotr Weltak</p>
      <p class="person-role">Fitoterapeuta</p>
    </div>

    <address class="address">
      Dąbrowa Sękowska 14,<br>38-415 Mielnik
    </address>

    <ul class="contact-list">
      <li>
        <svg viewBox="0 0 16 16" aria-hidden="true"><path d="M3.6 1.2l2.3 2.6-1.3 1.7c.9 2 2.2 3.3 4.2 4.2l1.7-1.3 2.6 2.3-1.3 2.4C6.7 13 3 9.3 1.2 4.8z"/></svg>
        <span>574 806 215</span>
      </li>
      <li>
        <svg viewBox="0 0 16 16" aria-hidden="true"><path d="M1 3h14v10H1z M2.2 4.2L8 8.6l5.8-4.4z" fill-rule="evenodd"/></svg>
        <span>piotrweltak@osrodekzielnika.com</span>
      </li>
      <li>
        <svg viewBox="0 0 16 16" aria-hidden="true"><circle cx="8" cy="8" r="7"/><path d="M1.5 8h13M8 1c-2.5 2.5-2.5 11.5 0 14M8 1c2.5 2.5 2.5 11.5 0 14" stroke="#2a2a2b" stroke-width="1.1" fill="none"/></svg>
        <span>www.<span class="web-highlight">osrodek-zielnika</span>.pl</span>
      </li>
    </ul>

    <div class="brand-mark">
      <div class="brand-dot"></div>
      <p class="brand-name">OSRODEK ZIELNIKA</p>
    </div>

    <div class="bottom-band"></div>
  </article>
</body>
</html>
```